Postcard Design

our company name is wexford lane haven.we provide face to face psychic tarot reading and crystal healing in a very exclusive and private clinic. we provide answers and guidance for future life event and the balance for the body and soul.we are base in 17 wexford lane in london .we want a card who say what we do as clear as possible and who is eye catching to people so when they see it want to read it this is our web site www.wexfordlnhaven.co.uk you need to put number on it to call us the number ContacUs:
0208 594 3216
0788 213 5072

Industry/Entity Type

Clinic

```html
<!DOCTYPE html>
<html lang="en">
<head>
<meta charset="utf-8">
<title>Wexford Lane Haven – Postcard</title>
<link rel="stylesheet" href="https://fonts.googleapis.com/css2?family=Alfa+Slab+One&family=Tinos:ital,wght@0,700;1,700&display=swap">
<style>
  :root {
    --page: #ffffff;
    --card-cream: #fbf6b4;
    --card-edge: #f0a048;
    --lime: #c9ef82;
    --lime-deep: #b6e06a;
    --wood: #c8a36a;
    --wood-dark: #a9834d;
    --board: #241b17;
    --board-edge: #3a2d26;
    --frame: #f7f3c9;
    --brand-ink: #1a1a1a;
    --contact-ink: #8b3a12;
    --web-ink: #2f4b12;
    --board-ink: #ffffff;
    --divider: #4a4a1e;
    --stamp-line: #111111;
  }
  * { margin: 0; padding: 0; box-sizing: border-box; }
  html, body { width: 1200px; height: 900px; overflow: hidden; background: var(--page); }
  .postcard {
    position: absolute; left: 37px; top: 37px; width: 1126px; height: 825px;
    background: var(--card-cream); overflow: hidden;
  }
  .edge-decor {
    position: absolute; inset: 0;
    background:
      radial-gradient(ellipse at 100% 0%, var(--card-edge) 0, rgba(240,160,72,0) 18%),
      radial-gradient(ellipse at 100% 100%, var(--card-edge) 0, rgba(240,160,72,0) 20%),
      radial-gradient(ellipse at 0% 100%, rgba(240,160,72,.7) 0, rgba(240,160,72,0) 16%),
      linear-gradient(to top, rgba(240,160,72,.55), rgba(240,160,72,0) 60px);
  }
  .heading-band {
    position: absolute; left: 0; top: 0; width: 646px; height: 221px;
    background: linear-gradient(180deg, var(--lime) 0%, var(--lime-deep) 100%);
  }
  .brand {
    position: absolute; left: 60px; top: 26px;
    font-family: "Tinos", serif; font-weight: 700; font-size: 44px;
    color: var(--brand-ink); letter-spacing: 1px; white-space: nowrap;
  }
  .contact {
    position: absolute; left: 143px; top: 86px;
    font-family: "Alfa Slab One", serif; color: var(--contact-ink);
    font-size: 26px; line-height: 30px; letter-spacing: 5.3px; white-space: nowrap;
  }
  .contact .label { font-size: 24px; letter-spacing: 4px; }
  .website {
    position: absolute; left: 146px; top: 185px;
    font-family: "Tinos", serif; font-style: italic; font-weight: 700;
    font-size: 28px; color: var(--web-ink); letter-spacing: 3.4px; white-space: nowrap;
  }
  .wood-panel {
    position: absolute; left: 0; top: 221px; width: 143px; height: 464px;
    background: linear-gradient(90deg, var(--wood) 0%, var(--wood-dark) 50%, var(--wood) 100%);
  }
  .board-frame {
    position: absolute; left: 143px; top: 221px; width: 503px; height: 487px;
    background: var(--frame);
  }
  .board {
    position: absolute; left: 156px; top: 241px; width: 475px; height: 449px;
    background: linear-gradient(160deg, var(--board-edge) 0%, var(--board) 40%, var(--board) 100%);
    box-shadow: 0 0 6px rgba(0,0,0,.5);
    font-family: "Tinos", serif; font-style: italic; font-weight: 700; color: var(--board-ink);
  }
  .board h2 {
    position: absolute; left: 19px; top: 16px; font-size: 38px; font-weight: 700;
    letter-spacing: 2.3px; white-space: nowrap;
  }
  .services {
    list-style: none; position: absolute; left: 32px; top: 60px;
    font-size: 32px; line-height: 44px; letter-spacing: 2.7px; white-space: nowrap;
  }
  .services li { position: relative; }
  .services li::before {
    content: ""; position: absolute; left: -19px; top: 20px; width: 10px; height: 10px;
    border-radius: 50%; background: var(--board-ink);
  }
  .divider { position: absolute; left: 646px; top: 0; width: 2px; height: 825px; background: var(--divider); }
  .address-area { position: absolute; left: 651px; top: 221px; width: 469px; height: 487px; background: #fff; }
  .stamp-box {
    position: absolute; left: 928px; top: 13px; width: 190px; height: 176px;
    background: #fff; border: 3px solid var(--stamp-line); box-shadow: 2px 3px 4px rgba(0,0,0,.35);
  }
</style>
</head>
<body>
  <div class="postcard">
    <div class="edge-decor" role="img" aria-label="Orange grass fringe and floral swirl ornaments around the card edges"></div>

    <section class="heading-band">
      <h1 class="brand">Wexford Lane Haven</h1>
      <p class="contact"><span class="label">Contac Us:</span><br>0208 594 3216<br>0788 213 5072</p>
      <p class="website">www.wexfordlnhaven.co.uk</p>
    </section>

    <div class="wood-panel" role="img" aria-label="Oak wood grain texture with a white floral spray ornament"></div>
    <div class="board-frame"></div>
    <section class="board">
      <h2>WE ARE PROVIDING ,</h2>
      <ul class="services">
        <li>face to face psychic<br>tarot reading</li>
        <li>crystal healing in a very<br>exclusive and private clinic</li>
        <li>answers and guidance for<br>future life event and the</li>
        <li>balance for the body and<br>soul ....,</li>
      </ul>
    </section>

    <div class="divider"></div>
    <div class="address-area"></div>
    <div class="stamp-box"></div>
  </div>
</body>
</html>
```